Business card design needed

Double sided
Color, unique, elegant

Maybe put this quote somewhere?? But I think it might make it to cluttered?
“The Pilates Method of Body
Conditioning develops the body
uniformly, corrects posture, restores
vitality, invigorates the mind and
elevates the spirit”
- Henrik Dovacombe

Industry/Entity Type

Business

Contact Information for Business Card

Marta Kellbrook
Pilates Instructor & Personal trainer
Mobile: 0498265043
www.lorvix.com.au
email: lorvixhealth.fitness@qentamail.com

```html
<!DOCTYPE html>
<html lang="en">
<head>
<meta charset="utf-8">
<title>Lorvix Health and Fitness – Business Card</title>
<link href="https://fonts.googleapis.com/css2?family=Open+Sans:wght@400;600&display=swap" rel="stylesheet">
<style>
  :root {
    --backdrop: #ececec;
    --card: #fbfbfb;
    --ink-grey: #6e6e70;
    --ink-soft: #9a9a9c;
    --ink-blue: #3a4a7a;
    --accent-purple: #b14fb0;
    --decor-grey: #d9d9d9;
  }
  * { margin: 0; padding: 0; box-sizing: border-box; }
  html, body {
    width: 1200px; height: 795px; overflow: hidden;
    background: var(--backdrop);
    font-family: "Open Sans", Arial, sans-serif;
  }
  .sheet {
    position: relative; width: 1200px; height: 795px;
    display: flex; align-items: center; justify-content: center; gap: 60px;
  }
  .card {
    position: relative; width: 525px; height: 300px;
    background: var(--card);
    box-shadow: 0 12px 30px rgba(0,0,0,0.10), 0 2px 6px rgba(0,0,0,0.06);
    overflow: hidden;
  }
  .card__decor {
    position: absolute; right: -40px; top: 30px;
    width: 230px; height: 300px;
    background: radial-gradient(ellipse at 60% 40%, var(--decor-grey) 0%, rgba(217,217,217,0.5) 45%, rgba(251,251,251,0) 72%);
  }
  /* front */
  .brand {
    position: absolute; left: 160px; top: 105px;
    display: flex; flex-direction: column; align-items: flex-start;
  }
  .brand__row { display: flex; align-items: center; gap: 10px; }
  .brand__dot { width: 14px; height: 14px; border-radius: 50%; background: var(--accent-purple); }
  .brand__name {
    font-size: 40px; font-weight: 400; letter-spacing: 3px;
    color: var(--ink-grey); line-height: 1;
  }
  .brand__tagline {
    margin-top: 8px; margin-left: 24px;
    font-size: 15px; color: var(--ink-grey); letter-spacing: 0.5px;
  }
  /* back */
  .back__brand {
    position: absolute; left: 180px; top: 22px;
    display: flex; flex-direction: column; align-items: center;
  }
  .back__brand .brand__name { font-size: 18px; letter-spacing: 2px; }
  .back__brand .brand__tagline { margin: 2px 0 0; font-size: 7px; }
  .contact { position: absolute; left: 36px; top: 72px; }
  .contact__name { font-size: 18px; color: var(--ink-grey); }
  .contact__role { font-size: 12px; font-weight: 600; color: var(--ink-blue); margin-top: 1px; }
  .contact__lines { margin-top: 12px; font-size: 11px; line-height: 1.45; color: var(--ink-grey); }
  .socials {
    position: absolute; left: 20px; right: 20px; bottom: 14px;
    display: flex; justify-content: space-between;
  }
  .social { display: flex; align-items: center; gap: 5px; font-size: 7.5px; color: var(--ink-soft); }
  .social__mark { width: 8px; height: 8px; background: var(--ink-soft); }
</style>
</head>
<body>
<main class="sheet">
  <section class="card card--front">
    <div class="card__decor" role="img" aria-label="Faint large brand decoration"></div>
    <div class="brand">
      <div class="brand__row">
        <span class="brand__dot"></span>
        <span class="brand__name">Lorvix</span>
      </div>
      <span class="brand__tagline">Health and Fitness</span>
    </div>
  </section>

  <section class="card card--back">
    <div class="card__decor" role="img" aria-label="Faint large brand decoration"></div>
    <div class="back__brand">
      <span class="brand__name">Lorvix</span>
      <span class="brand__tagline">Health and Fitness</span>
    </div>
    <div class="contact">
      <p class="contact__name">Marta Kellbrook Pilates</p>
      <p class="contact__role">Instructor &amp; Personal trainer</p>
      <div class="contact__lines">
        <p>0498265043</p>
        <p>lorvixhealth.fitness@qentamail.com</p>
        <p>www.lorvix.com.au</p>
      </div>
    </div>
    <div class="socials">
      <span class="social"><span class="social__mark"></span>name.pagenest.com</span>
      <span class="social"><span class="social__mark"></span>name.chirpline.com</span>
      <span class="social"><span class="social__mark"></span>name.circleplus.com</span>
    </div>
  </section>
</main>
</body>
</html>
```